Digital Album Cover - Piano music for wedding ceremonies and receptions

I need cover art for a piano album project that will be distributed to TuneVault, Wavelane etc. Covert art required for front of album. At this stage physical CDs will not be printed nor required it is just a digital release.
Artist name: Toby Hargrove
Album Title: Gentle Keys Melodies Wedding Ceremonies and Receptions
Volume 3
Sample piano songs are on my tunecast page
https://tunecast.example/tobyhargrovekeys/sets/gentle-keys-melodies-vol-3
Previous album artwork used from sketch hive competitions winners
https://musicvault.example/au/artist/toby-hargrove/4830917265
Target Market(s)
brides to be
grooms to be
people interested in weddings
people enjoy love songs or easy listening music
Industry/Entity Type
Wedding
Look and feel
Each slider illustrates characteristics of the customer's brand and the style your logo design should communicate.

```html
<!DOCTYPE html>
<html lang="en">
<head>
<meta charset="utf-8">
<title>Toby Hargrove – Gentle Keys Melodies Vol. 3</title>
<link rel="stylesheet" href="https://fonts.googleapis.com/css2?family=Great+Vibes&family=Montserrat:wght@400;500&display=swap">
<style>
  :root {
    --veil-light: #f1f0f2;
    --veil-mid: #dcdbde;
    --veil-grey: #c9c7cb;
    --photo-skin: #d9b8a4;
    --photo-hair: #c9a67a;
    --photo-suit: #1e1c1f;
    --photo-dress: #eeeeef;
    --gold-light: #f7df86;
    --gold: #d9a92b;
    --gold-deep: #a87712;
    --ink: #111111;
  }
  * { margin: 0; padding: 0; box-sizing: border-box; }
  html, body { width: 1200px; height: 1200px; overflow: hidden; background: var(--veil-light); }
  .album-cover {
    position: relative;
    width: 1200px;
    height: 1200px;
    overflow: hidden;
    background: linear-gradient(160deg, var(--veil-light) 0%, var(--veil-mid) 45%, var(--veil-light) 100%);
  }
  .couple-photo, .frame-lines, .ornament {
    position: absolute;
    inset: 0;
  }
  .ornament {
    inset: auto;
    left: 24px; top: 30px;
    width: 340px; height: 226px;
    border-radius: 50%;
    background: radial-gradient(ellipse at 40% 50%, rgba(231,185,64,0.55) 0%, rgba(231,185,64,0.18) 50%, rgba(231,185,64,0) 72%);
  }
  .artist-name {
    position: absolute;
    left: 108px;
    top: 540px;
    font-family: "Great Vibes", cursive;
    font-weight: 400;
    font-size: 158px;
    line-height: 0.95;
    background: linear-gradient(180deg, var(--gold-light) 0%, var(--gold) 55%, var(--gold-deep) 100%);
    -webkit-background-clip: text;
    background-clip: text;
    color: transparent;
  }
  .artist-name span { display: block; }
  .artist-name .surname { padding-left: 56px; }
  .album-title {
    position: absolute;
    left: 106px;
    top: 1026px;
    font-family: "Montserrat", sans-serif;
    font-weight: 400;
    font-size: 52px;
    letter-spacing: 1px;
    color: var(--ink);
    text-transform: uppercase;
    white-space: nowrap;
  }
  .album-subtitle {
    position: absolute;
    left: 110px;
    top: 1122px;
    font-family: "Montserrat", sans-serif;
    font-weight: 400;
    font-size: 20px;
    letter-spacing: 1.5px;
    color: var(--ink);
    text-transform: uppercase;
    white-space: nowrap;
  }
  .volume {
    position: absolute;
    left: 880px;
    top: 1000px;
    font-family: "Great Vibes", cursive;
    font-size: 120px;
    line-height: 1;
    background: linear-gradient(180deg, var(--gold-light) 0%, var(--gold) 55%, var(--gold-deep) 100%);
    -webkit-background-clip: text;
    background-clip: text;
    color: transparent;
    white-space: nowrap;
  }
</style>
</head>
<body>
<main class="album-cover">
  <svg class="couple-photo" role="img" aria-label="Photograph of a bride and groom embracing beneath a flowing white veil, the groom kissing her forehead while she holds white orchids" width="1200" height="1200" viewBox="0 0 1200 1200">
    <defs>
      <linearGradient id="photoTone" x1="0" y1="0" x2="1" y2="0.3">
        <stop offset="0" stop-color="var(--photo-hair)"/>
        <stop offset="0.3" stop-color="var(--photo-skin)"/>
        <stop offset="0.55" stop-color="var(--photo-dress)"/>
        <stop offset="0.75" stop-color="var(--photo-suit)"/>
        <stop offset="1" stop-color="var(--photo-suit)"/>
      </linearGradient>
      <linearGradient id="veilFade" x1="0" y1="0" x2="1" y2="1">
        <stop offset="0" stop-color="#ffffff" stop-opacity="0.85"/>
        <stop offset="1" stop-color="#ffffff" stop-opacity="0"/>
      </linearGradient>
    </defs>
    <path d="M560 0 H1200 V1200 H780 C700 1050 620 800 600 560 C585 380 640 180 560 0 Z" fill="url(#photoTone)"/>
    <path d="M0 0 H820 C700 120 640 300 620 470 C600 640 650 900 560 1200 H0 Z" fill="url(#veilFade)"/>
  </svg>

  <div class="ornament" role="img" aria-label="Gold glitter flourish ornament"></div>

  <svg class="frame-lines" width="1200" height="1200" viewBox="0 0 1200 1200" aria-hidden="true">
    <defs>
      <linearGradient id="goldLine" x1="0" y1="0" x2="0" y2="1">
        <stop offset="0" stop-color="var(--gold-light)"/>
        <stop offset="0.5" stop-color="var(--gold)"/>
        <stop offset="1" stop-color="var(--gold-deep)"/>
      </linearGradient>
    </defs>
    <path d="M300 106 H744" stroke="var(--gold)" stroke-width="3" fill="none"/>
    <path d="M44 234 V1090 Q44 1128 82 1128 H146" stroke="url(#goldLine)" stroke-width="4" fill="none"/>
  </svg>

  <h1 class="artist-name"><span class="given">Toby</span><span class="surname">Hargrove</span></h1>
  <p class="album-title">Gentle Keys Melodies</p>
  <p class="album-subtitle">Wedding Ceremonies and Receptions</p>
  <p class="volume">Vol. 3</p>
</main>
</body>
</html>
```